Coming Soon page for a new fitness startup

We are a new startup based in Toronto, Canada working on a site and mobile app where people can register for athletic events such as running, cycling, triathlon, SUP, etc.

Participants will also be able to manage their clubs and team, and connect their fitness trackers so they have all their fitness data and friends in one place.

I like very simple designs and lots of whitespace. So no need for icons or unnecessary graphics.

I prefer having a mobile phone app instead of a hero image. No need to worry about the details within the mobile app for now, we can fill it in later. Here are some landing pages that I like.
https://pixelvault.example/torvanmelk/buckets/438197-Landing-Page

Attached is a wireframe that gives some sample content for each of the sections. Please do not take the wireframe too literally, it is only meant to illustrate the content that we are experimenting with and should give an idea of how much text will be on the page.

I have also attached the company logo files. The logo is not being used yet so feel free to simplify the logo if it doesn't look great with your design. For example, I'm ok with just the name "k7ravi" in white if that looks better.

Target Market(s)

Ages 25 to 45. Interested in running, cycling, triathlon, SUP, etc.

Industry/Entity Type

Fitness

Coding

Coded - Design and coding required

Number of Pages Required

1 page

Requirements
Should not have
• Any photos should not contain track and field events, or people in a gym. Any photos should have people running or cycling outdoors. I know that photos can be easily swapped out but it is distracting to review a design that has the wrong photos.

```html
<!DOCTYPE html>
<html lang="en">
<head>
<meta charset="utf-8">
<title>k7ravi — Launching in Spring 2018</title>
<link href="https://fonts.googleapis.com/css2?family=Montserrat:wght@500;600;700&family=Open+Sans:ital,wght@0,400;0,600;0,700;1,600&display=swap" rel="stylesheet">
<style>
:root{
  --red:#d32235;
  --red-dark:#8e1723;
  --ink:#2b2b2b;
  --text:#4a4a4a;
  --soft:#f7f7f7;
  --field:#efefef;
  --frame:#e4e4e4;
  --white:#ffffff;
  --charcoal:#333333;
}
*{box-sizing:border-box;margin:0;padding:0}
html,body{width:804px;height:1200px;overflow:hidden}
body{background:var(--frame);font-family:"Open Sans",Arial,sans-serif;color:var(--text)}
.page{position:absolute;left:10px;top:10px;width:784px;height:1180px;background:var(--white);overflow:hidden}
.abs{position:absolute}

/* hero */
.hero-bg{position:absolute;left:0;top:0}
.brand{left:26px;top:24px;font-family:"Montserrat",sans-serif;font-weight:600;font-size:26px;color:var(--white);letter-spacing:.5px}
.launch{left:568px;top:31px;font-family:"Montserrat",sans-serif;font-weight:600;font-size:12px;color:var(--white);letter-spacing:.3px}
.hero-copy{left:275px;top:130px;width:480px;color:var(--white)}
.hero-kicker{font-family:"Montserrat",sans-serif;font-weight:700;font-size:18.5px;line-height:22px;letter-spacing:-.2px}
.hero-title{font-family:"Montserrat",sans-serif;font-weight:700;font-size:37px;line-height:36px;margin-bottom:16px}
.hero-text{font-size:11px;line-height:15.3px;letter-spacing:-.2px}
.signup-title{margin-top:30px;font-family:"Open Sans",sans-serif;font-weight:600;font-size:16.5px}
.signup-sub{margin-top:9px;font-size:10.5px;font-weight:600}
.email-row{display:flex;gap:6px;margin-top:10px;margin-left:-3px}
.email-input{width:311px;height:35px;border-radius:18px;background:var(--field);border:2px solid #d9d9d9;font:600 11px "Open Sans",sans-serif;color:var(--charcoal);padding-left:16px;display:flex;align-items:center}
.notify-btn{width:112px;height:35px;border-radius:18px;background:var(--charcoal);border:2px solid #e8e8e8;color:var(--white);font:600 12.5px "Montserrat",sans-serif;letter-spacing:.5px;display:flex;align-items:center;justify-content:center}

/* phone */
.phone{left:45px;top:109px;width:175px;height:346px}
.phone-shadow{left:20px;top:448px;width:230px;height:14px;border-radius:50%;background:radial-gradient(ellipse,rgba(0,0,0,.18),rgba(0,0,0,0) 70%)}
.screen-brand{left:45px;top:143px;width:175px;text-align:center;font-family:"Montserrat",sans-serif;font-weight:600;font-size:19px;color:var(--red)}
.screen-photo{left:56px;top:178px;width:150px;height:100px;background:linear-gradient(160deg,#9a9a9a,#5c5c5c 60%,#7b7b7b)}
.screen-card{left:56px;top:278px;width:150px;height:112px;background:#3a3a3a}
.avatar{left:106px;top:254px;width:50px;height:50px;border-radius:50%;background:linear-gradient(#8a8a8a,#4d4d4d);border:2px solid var(--white);box-shadow:0 0 0 1.5px #222}
.athlete{left:56px;top:311px;width:150px;text-align:center;color:var(--white);font-style:italic;font-weight:600;font-size:8px;line-height:11px}
.athlete small{display:block;font-size:6.5px}
.stars{left:56px;top:341px;width:150px;text-align:center;color:#f4c430;font-size:10px;letter-spacing:1px}
.events-pill{left:83px;top:362px;width:98px;height:16px;border:1.5px solid var(--white);border-radius:9px;color:var(--white);font:700 7px "Open Sans",sans-serif;display:flex;justify-content:space-between;align-items:center;padding:0 10px}
.tabbar{left:56px;top:395px;width:168px;height:50px;display:flex}
.tab{flex:1;display:flex;flex-direction:column;align-items:center;justify-content:flex-end;padding-bottom:6px;font-size:5.5px;color:#555;border-right:1px solid #e3e3e3}
.tab:last-child{border-right:none}
.tab svg{margin-bottom:4px}

/* features */
.intro{left:0;top:533px;width:784px;text-align:center}
.intro h2{font-weight:600;font-size:17px;color:var(--ink)}
.intro p{margin-top:6px;font-weight:600;font-size:13.5px;color:var(--red)}
.feature{top:619px;width:205px}
.feature h3{font-weight:600;font-size:13px;color:var(--red);margin-bottom:8px}
.feature p{font-size:11px;line-height:15.5px;color:var(--text)}

/* events */
.events{left:0;top:766px;width:784px;height:372px;background:var(--soft)}
.organize{left:42px;top:72px;width:380px;color:var(--ink)}
.organize h2{font-weight:600;font-size:17px;margin-bottom:18px}
.organize p{font-weight:600;font-size:10.5px;line-height:15.3px;margin-bottom:15px}
.contact{left:491px;top:63px;width:247px;height:247px;background:var(--white);box-shadow:0 8px 10px -6px rgba(0,0,0,.18)}
.contact-head{height:34px;background:var(--red);color:var(--white);font:600 12.5px "Montserrat",sans-serif;display:flex;align-items:center;justify-content:center;letter-spacing:.2px}
.contact-body{padding:12px 19px 0}
.field-label{font-weight:600;font-size:8px;color:var(--ink);margin-bottom:5px}
.field-label b{color:var(--red)}
.field{height:17px;background:var(--field);margin-bottom:11px}
.field.area{height:61px;margin-bottom:7px}
.submit{width:91px;height:21px;background:var(--charcoal);color:var(--white);font-weight:700;font-size:9.5px;display:flex;align-items:center;justify-content:center}

/* footer */
.footer{left:0;top:1138px;width:784px;height:42px;display:flex;align-items:center;justify-content:space-between;padding:0 13px 0 13px;font-weight:600;font-size:8.5px;color:var(--ink);border-top:1px solid #eee}
.footer-links span{margin:0 5px}
.social{display:flex;gap:2px;margin-left:30px}
.social i{width:15px;height:15px;border:1.3px solid var(--ink);border-radius:50%;display:block}
</style>
</head>
<body>
<div class="page">

  <svg class="hero-bg" width="784" height="480" viewBox="0 0 784 480" aria-hidden="true">
    <polygon points="0,0 784,0 784,472 0,410" fill="var(--red)"/>
    <polygon points="462,0 784,0 784,80 541,80" fill="var(--red-dark)"/>
  </svg>

  <div class="abs brand">k7ravi</div>
  <div class="abs launch">LAUNCHING IN SPRING 2018</div>

  <div class="abs hero-copy">
    <div class="hero-kicker">CONNECT YOUR TRAINING, FRIENDS AND EVENTS</div>
    <h1 class="hero-title">IN ONE PLACE</h1>
    <p class="hero-text">Lorem ipsum dolor sit amet, consectetuer adipiscing elit, sed diam nonummy nibh euismod tincidunt ut laoreet dolore magna aliquam erat volutpat. Ut wisi enim ad minim veniam, quis nostrud exerci tati on ullamcorper suscipit lobortis nisl ut aliquip ex ea commodo consequat. Duis autem vel eum iriure dolor in hendrerit in vulputate velit esse molestie consequat.</p>
    <h2 class="signup-title">Join our email list</h2>
    <p class="signup-sub">A referral program is coming and you'll want to be the first to know</p>
    <div class="email-row">
      <div class="email-input">Email Address</div>
      <div class="notify-btn">NOTIFY ME</div>
    </div>
  </div>

  <!-- app phone -->
  <div class="abs phone-shadow"></div>
  <svg class="abs phone" viewBox="0 0 175 346" aria-hidden="true">
    <rect x="1" y="1" width="173" height="344" rx="24" fill="#f4f4f4" stroke="#3a3a3a" stroke-width="2"/>
    <rect x="5" y="5" width="165" height="336" rx="20" fill="var(--white)" stroke="#9a9a9a" stroke-width="1"/>
    <path d="M42 5 h91 v4 a8 8 0 0 1 -8 8 h-75 a8 8 0 0 1 -8 -8z" fill="#1f1f1f"/>
    <rect x="-2" y="55" width="3" height="14" fill="#222"/>
    <rect x="-2" y="80" width="3" height="24" fill="#222"/>
    <rect x="-2" y="110" width="3" height="24" fill="#222"/>
    <rect x="174" y="85" width="3" height="36" fill="#222"/>
  </svg>
  <div class="abs screen-brand">k7ravi</div>
  <div class="abs screen-photo" role="img" aria-label="Black and white photo of cyclists racing outdoors"></div>
  <div class="abs screen-card"></div>
  <div class="abs avatar" role="img" aria-label="Athlete profile picture"></div>
  <div class="abs athlete">Marco Lindqvist<small>San Francisco, California</small></div>
  <div class="abs stars">★★★★★</div>
  <div class="abs events-pill"><span>EVENTS</span><span>&gt;10</span></div>
  <div class="abs tabbar" style="width:150px">
    <div class="tab"><svg width="18" height="16" viewBox="0 0 18 16"><g fill="#444"><rect x="0" y="1" width="3" height="2"/><rect x="5" y="1" width="13" height="2"/><rect x="0" y="7" width="3" height="2"/><rect x="5" y="7" width="13" height="2"/><rect x="0" y="13" width="3" height="2"/><rect x="5" y="13" width="13" height="2"/></g></svg>EVENTS</div>
    <div class="tab"><svg width="18" height="10" viewBox="0 0 18 10"><g fill="none" stroke="#444" stroke-width="1"><circle cx="3" cy="3" r="2"/><circle cx="9" cy="3" r="2"/><circle cx="15" cy="3" r="2"/><path d="M0 9c0-2 6-2 6 0M6 9c0-2 6-2 6 0M12 9c0-2 6-2 6 0"/></g></svg>TEAMS</div>
    <div class="tab"><svg width="16" height="18" viewBox="0 0 16 18"><g fill="#444"><circle cx="8" cy="5" r="4.5"/><path d="M0 18c0-6 16-6 16 0z"/></g></svg>PROFILE</div>
    <div class="tab"><svg width="10" height="18" viewBox="0 0 10 18"><g fill="#444"><rect x="2" y="0" width="6" height="3"/><rect x="2" y="15" width="6" height="3"/><rect x="1" y="3" width="8" height="12" rx="2" fill="none" stroke="#444" stroke-width="1.5"/></g></svg>DEVICES</div>
  </div>

  <!-- features -->
  <div class="abs intro">
    <h2>Training and Racing all in one place</h2>
    <p>A new fitness community is coming soon</p>
  </div>
  <div class="abs feature" style="left:47px">
    <h3>Sign up for events</h3>
    <p>Lorem ipsum dolor sit amet, consectetue adipiscing elit, sed diam nonummy nibh euismod tincidunt ut laoreet dolore mag aliquam erat volutpat.</p>
  </div>
  <div class="abs feature" style="left:295px">
    <h3>Invite your friends</h3>
    <p>Lorem ipsum dolor sit amet, consectetue adipiscing elit, sed diam nonummy nibh euismod tincidunt ut laoreet dolore mag aliquam erat volutpat.</p>
  </div>
  <div class="abs feature" style="left:542px">
    <h3>Connect your workouts</h3>
    <p>Lorem ipsum dolor sit amet, consectetue adipiscing elit, sed diam nonummy nibh euismod tincidunt ut laoreet dolore mag aliquam erat volutpat.</p>
  </div>

  <!-- events organizer -->
  <section class="abs events">
    <div class="abs organize">
      <h2>Organizing an event?</h2>
      <p>Attracting participants is hard work.</p>
      <p>With your event listed on k7ravi, we'll not only handle the registration and payment process, we've also made it our own personal mission to drive up participation numbers across all events.An online presence requires effort and planning.</p>
      <p>Contact us to learn more.</p>
    </div>
    <div class="abs contact">
      <div class="contact-head">WE'D LOVE TO HEAR FROM YOU</div>
      <div class="contact-body">
        <div class="field-label">Your name<b>*</b></div>
        <div class="field"></div>
        <div class="field-label">Email address<b>*</b></div>
        <div class="field"></div>
        <div class="field-label">How can we help?</div>
        <div class="field area"></div>
        <div class="submit">SUBMIT</div>
      </div>
    </div>
  </section>

  <footer class="abs footer">
    <div class="footer-links">About Us<span>I</span>Developers<span>I</span>Careers</div>
    <div class="social"><i></i><i></i><i></i></div>
    <div>Copyright © 2018 k7ravi, Inc.</div>
  </footer>
</div>
</body>
</html>
```